Yearly symposium in equestrian ethology needs a poster

We need a poster for a Yearly symposium in equestrian ethology. Ethology = science which studies animal behaviours. In our case horses behaviours.
Our principal and basic thematic is "the contribution of the ethology to the human-horse relationship".
This poster wil have to be a lay out which will be used each year with an update of the content, photos following the theme.
the original file, fonts or other graphics will have to be provided with the final project. Do not forget that you will probably design it in english and we will have to translate it in french.
Through this visual we want to communicate: science, rigorous, relationship, respect and wellness of horses and human - harmony. We want to encourage critical thinking.
This year the theme will be "is the horse a therapist?"

Enclosed you will find the poster for the symposium 2013

The final amount will have to be invoiced.

Reason: I will be on vacation from Aug 12 till 19. I'll give feedback to your projects and posted comments when I return

Anyone wanting to improve their relationship with horses. Most of participnats are women but not only. Age: between 20 and 50.

Wellness

• Place to add pratical info: date, place, title of the symposium etc.

```html
<!DOCTYPE html>
<html lang="en">
<head>
<meta charset="utf-8">
<title>Equine Ethology Symposium</title>
<link href="https://fonts.googleapis.com/css2?family=Mulish:wght@400;600;800&display=swap" rel="stylesheet">
<style>
:root{
  --maroon:#3b1813;
  --maroon-shade:#5c2f26;
  --panel:#dcf0f8;
  --ink:#2e1510;
  --photo-light:#9cc25a;
  --photo-mid:#6f9a3c;
  --photo-horse:#a8562a;
}
*{margin:0;padding:0;box-sizing:border-box}
html,body{width:928px;height:1200px;overflow:hidden}
body{background:var(--maroon);font-family:'Mulish',sans-serif;color:var(--ink);position:relative}
.panel{position:absolute;left:58px;width:814px;background:var(--panel);text-align:center}
.panel::before{content:"";position:absolute;z-index:-1;background:var(--maroon-shade)}
.header{top:0;height:201px;padding-top:30px}
.header::before{left:-8px;right:14px;bottom:-10px;height:20px}
.event-title{font-weight:800;font-size:33px;letter-spacing:.5px;line-height:1.1}
.event-date{font-weight:600;font-size:25px;margin-top:6px}
.venue{font-size:18px;line-height:1.6;margin-top:8px}
.photo{position:absolute;left:210px;top:181px;width:514px;height:684px;
  background:linear-gradient(100deg,var(--photo-horse) 0%,#8a4a26 38%,var(--photo-mid) 55%,var(--photo-light) 100%)}
.footer{top:880px;height:320px;padding-top:24px;z-index:2}
.footer::before{left:-8px;right:16px;top:-10px;height:20px}
.theme-intro{font-size:17px}
.theme-title{font-weight:600;font-size:24px;margin-top:6px}
.topics{font-size:19px;line-height:1.4;margin-top:8px}
.speakers{list-style:none;font-size:16px;line-height:1.45;margin-top:8px}
.practical{font-size:16px;line-height:1.45;margin-top:8px}
.practical strong{font-weight:800}
</style>
</head>
<body>
<header class="panel header">
  <h1 class="event-title">EQUINE ETHOLOGY SYMPOSIUM</h1>
  <p class="event-date">Saturday 29 March 2014 from 8:30 am to 6:00 pm</p>
  <p class="venue">Université de Valbrise<br>Valbrise, Auditorium B12, Faculty of Sciences, rue des Tilleuls</p>
</header>

<div class="photo" role="img" aria-label="Photo of a woman resting her head gently against a chestnut horse, green meadow behind"></div>

<section class="panel footer">
  <p class="theme-intro">The contribution of ethology to the human-horse relationship – 2014 Edition:</p>
  <h2 class="theme-title">“Is the horse a therapist?”</h2>
  <p class="topics">Equine-assisted therapy: evidence and limits,…<br>Psychological aspects of the human in the relationship</p>
  <ul class="speakers">
    <li>Lena Hofstede, Universiteit Oosterveld, Netherlands</li>
    <li>Paul Dessart, Université de Brennemont, Brennemont</li>
    <li>Luc Verhaegen, Faculty of Veterinary Medicine, Morlanval</li>
  </ul>
  <p class="practical">Fee: adults €50 (€60 on site) – students €25 (€30 on site)<br>
  Lunch included - limited number of seats.<br>
  Information and registration on the website: <strong>www.colloque-equin.org</strong></p>
</section>
</body>
</html>
```